Education business partners flyer

Our service is New Zealand education and migration. We are trying to recruit business partners from around the world who can refer clients to us. We need a 2-3 page PDF flyer that we want to share with our prospective partners. Our content is ready (file attached). It needs to be designed well with relevant NZ images, international students/migrants and our logo of course.

Target Market(s)

All around the world

Industry/Entity Type

Education

Font styles to use
Sans Serif

Colors

Designer to choose colors to be used in the design.

Requirements
Must have
• It needs to be designed well with relevant NZ images, international students/migrants and our logo of course.
Nice to have
• Copyright free images.
Should not have
• Images with any copyright issues.

```html
<!DOCTYPE html>
<html lang="en">
<head>
<meta charset="utf-8">
<title>NVX – New Zealand Education &amp; Migration Partner Flyer</title>
<link href="https://fonts.googleapis.com/css2?family=Raleway:wght@300;400;600;700&family=PT+Sans+Narrow:wght@400;700&family=Open+Sans:wght@400;600&display=swap" rel="stylesheet">
<style>
  :root{
    --purple:#7b1883;
    --purple-deep:#65106b;
    --ink:#3d3d3d;
    --grey-head:#4a4a4a;
    --panel:#4d4d4f;
    --gold:#f2b705;
    --rule:#b9b9b9;
    --white:#ffffff;
    --sky-top:#f3f5f8;
    --sky-mid:#dfe5ec;
    --city:#8aa0b6;
    --city-dark:#5f7890;
  }
  *{box-sizing:border-box;margin:0;padding:0}
  html,body{width:1016px;height:1200px;overflow:hidden;background:#e4e4e4}
  .flyer{position:relative;width:1016px;height:1200px;background:var(--white);font-family:"Open Sans",sans-serif;color:var(--ink)}

  /* Header */
  .hero{position:absolute;left:0;top:0;width:1016px;height:410px;
    background:linear-gradient(180deg,var(--white) 0%,var(--sky-top) 35%,var(--sky-mid) 62%,var(--city) 80%,var(--city-dark) 94%,#9fa7ad 100%)}
  .hero-rule{position:absolute;left:0;top:410px;width:1016px;height:8px;background:var(--purple);border-top:2px solid var(--gold)}
  .brand{position:absolute;left:60px;top:60px;display:flex;align-items:center;gap:12px;
    font-family:"Raleway",sans-serif;font-weight:700;font-size:46px;color:#111;letter-spacing:1px}
  .brand-dot{width:18px;height:18px;border-radius:50%;background:#111}
  .headline{position:absolute;left:40px;top:178px;font-family:"Raleway",sans-serif;line-height:1.08}
  .headline .country{display:block;font-weight:700;font-size:44px;color:var(--purple)}
  .headline .sector{display:block;font-weight:400;font-size:42px;color:var(--grey-head)}
  .headline .offer{display:block;font-weight:400;font-size:42px;color:var(--purple)}

  /* Intro boxes */
  .intro{position:absolute;left:40px;top:446px;width:936px;display:flex;justify-content:space-between}
  .intro-box{width:296px;height:252px;border:1px solid var(--rule);padding:4px 16px 12px;
    box-shadow:1px 1px 2px rgba(0,0,0,.12)}
  .intro-box legend{font-family:"PT Sans Narrow",sans-serif;font-weight:700;font-size:16px;color:#222;
    padding:0 8px;margin:0 auto;white-space:nowrap}
  .intro-box p{font-size:12.5px;line-height:17.5px;text-align:justify;text-align-last:center;color:#333;margin-top:4px}

  /* Highlights panel */
  .highlights{position:absolute;left:28px;top:735px;width:960px;height:395px;background:var(--panel);
    border-radius:10px;padding:40px 30px 16px;display:flex;gap:40px}
  .highlights-tab{position:absolute;left:50%;top:-14px;transform:translateX(-50%);background:var(--purple);
    color:var(--white);font-family:"Raleway",sans-serif;font-weight:700;font-size:19px;padding:9px 30px;
    white-space:nowrap;box-shadow:0 3px 6px rgba(0,0,0,.25)}
  .highlight-col{flex:1}
  .highlight h3{font-family:"Raleway",sans-serif;font-weight:400;font-size:16px;color:var(--gold);margin-bottom:6px}
  .highlight p{font-size:11.8px;line-height:16px;color:var(--white);text-align:justify}
  .highlight + .highlight{margin-top:16px}

  /* Footer */
  .contact-bar{position:absolute;left:0;top:1142px;width:1016px;height:58px;background:var(--purple-deep);
    display:flex;justify-content:center;align-items:center;gap:44px;color:var(--white);
    font-family:"Raleway",sans-serif;font-size:15px}
  .contact-item{display:flex;align-items:center;gap:8px}
  .contact-item svg{width:18px;height:18px}
</style>
</head>
<body>
<div class="flyer">

  <header>
    <div class="hero" role="img" aria-label="Photo of the Auckland city skyline across the harbour under a pale cloudy sky"></div>
    <div class="hero-rule"></div>
    <div class="brand"><span class="brand-dot"></span>NVX</div>
    <h1 class="headline">
      <span class="country">NEW ZEALAND</span>
      <span class="sector">Education &amp; migration</span>
      <span class="offer">Business opportunity</span>
    </h1>
  </header>

  <section class="intro">
    <fieldset class="intro-box">
      <legend>Why New Zealand and who is NVX?</legend>
      <p>New Zealand is booming as an education &amp; migration destination. In a world that is spiralling out of control; the serenity, safety and opportunities of New Zealand are attracting people from everywhere like a magnet. Numbers have been growing dramatically year on year. We are a deeply committed New Zealand education &amp; migration company, seeking to attract the best talent from around the world to make New Zealand their new home.</p>
    </fieldset>
    <fieldset class="intro-box">
      <legend>Why collaborate with NVX?</legend>
      <p>Collaborations can accelerate mutual growth in a globalised world. Our rationale in this proposal is that we do not have the reach in your market and vice versa you do not have a presence or team in New Zealand to continue to service your students or clients once they arrive here. By coming together we can achieve both these mutual objectives and create a viable and mutual business opportunity.</p>
    </fieldset>
    <fieldset class="intro-box">
      <legend>What is the NVX partnership framework?</legend>
      <p>We propose to work with you as our Referral Partner. A partnership that can be mutually beneficial and enhance the value of international education &amp; migration to deserving students and clients from everywhere. Our levels of association can vary depending on your current focus and how you can utilise our position especially in the areas of services that can only be rendered by a Licensed Immigration Adviser.</p>
    </fieldset>
  </section>

  <section class="highlights">
    <h2 class="highlights-tab">What are the highlights of NVX?</h2>
    <div class="highlight-col">
      <article class="highlight">
        <h3>We are New Zealand owned and based:</h3>
        <p>Hence we are able to provide services to clients in an end-to-end fashion from suggesting the right courses at the very beginning of their journey to hand-holding them all the way to employment and eventual residency in New Zealand. By working with us you not only create a viable business opportunity but can also be assured that your students/clients are in safe hands after they reach New Zealand. This is where the real challenges start for these young people as they need a huge amount of onshore support and guidance which we can provide.</p>
      </article>
      <article class="highlight">
        <h3>We have the full range of institutions:</h3>
        <p>We represent the entire gamut of quality New Zealand institutions and in the event your student needs/deserves the appropriate institution to fulfill their future aspirations, we can provide this opportunity for them together. We believe each student deserves to be in the institution that best serves their future interests and we can provide this opportunity for them.</p>
      </article>
    </div>
    <div class="highlight-col">
      <article class="highlight">
        <h3>We have an experienced team and great software:</h3>
        <p>Our competent counseling team backed by a visa team (including ex- New Zealand immigration officers) will ensure that each student is matched to the right course, college, city and to a career of his choice. Your student's parents will be extremely satisfied since their child will be taken care of in a professional manner. We have also built our inhouse software to streamline all processes and partners will have access to their own login for management of their prospects. Not to forget our impressive Board of Advisers who are senior ex- NZ government officials and professionals.</p>
      </article>
      <article class="highlight">
        <h3>We have a very high visa success rate:</h3>
        <p>Our current visa success rate for the first quarter of 2018 sits well above 90% and we aim to maintain this and keep improving on it successfully. Last year it was 80%. As you are aware a visa process is a detailed legal matter, our processes will ensure that your students have a very high chance of success in their visa applications. This means you can focus on your core strength as a marketer and garner prospective students and leave the admission and visa process to an established and successful team.</p>
      </article>
    </div>
  </section>

  <footer class="contact-bar">
    <span class="contact-item">
      <svg viewBox="0 0 24 24" fill="none" stroke="currentColor" stroke-width="1.8" stroke-linecap="round" stroke-linejoin="round"><path d="M22 16.9v3a2 2 0 0 1-2.2 2 19.8 19.8 0 0 1-8.6-3.1 19.5 19.5 0 0 1-6-6A19.8 19.8 0 0 1 2.1 4.2 2 2 0 0 1 4.1 2h3a2 2 0 0 1 2 1.7c.1 1 .4 1.9.7 2.8a2 2 0 0 1-.5 2.1L8 9.9a16 16 0 0 0 6 6l1.3-1.3a2 2 0 0 1 2.1-.4c.9.3 1.8.6 2.8.7a2 2 0 0 1 1.8 2z"/></svg>
      +91-9000012345
    </span>
    <span class="contact-item">
      <svg viewBox="0 0 24 24" fill="none" stroke="currentColor" stroke-width="1.8" stroke-linejoin="round"><rect x="3" y="5" width="18" height="14" rx="1"/><path d="M3 6l9 7 9-7"/></svg>
      partners@nvx.kiwi
    </span>
    <span class="contact-item">
      <svg viewBox="0 0 24 24" fill="none" stroke="currentColor" stroke-width="1.8"><circle cx="12" cy="12" r="9"/><path d="M3 12h18M12 3c3 3.2 3 14.8 0 18M12 3c-3 3.2-3 14.8 0 18"/></svg>
      www.nvx.kiwi
    </span>
  </footer>

</div>
</body>
</html>
```